Tavrion Engineering Report Template

A word doc report Template for an Engineering Company - Tavrion

Target Market(s)

Construction/Development Industry

Industry/Entity Type

Engineering Consultant

Font styles to use
Sans Serif
Other font styles liked:
• Calibri

Colors
0455a3

Requirements
Must have
• An awesome front page, using the Tavrion Logo (not sure which version yet)
• A great back page
• Good formatting within, different heading styles which look awesome
• Format generally as the the KWP example report, no need to vary
Nice to have
• smart features? easily manipulated? not sure how tricky or smart Word is in this area.
Should not have
• LOCKED features (if possible)

```html
<!DOCTYPE html>
<html lang="en">
<head>
<meta charset="utf-8">
<title>Tavrion Engineering Report Template – Covers</title>
<link rel="stylesheet" href="https://fonts.googleapis.com/css2?family=Open+Sans:wght@400;600;700&display=swap">
<style>
  :root {
    --backdrop: #c8d5d3;
    --brand-blue: #1654ab;
    --bright-blue: #2583e8;
    --steel-grey: #7e8f8d;
    --navy-shade: #172b4c;
    --paper: #ffffff;
    --ink: #1a1a1a;
    --pattern-tint: #3a74c4;
  }
  html, body {
    margin: 0;
    width: 1200px;
    height: 1200px;
    overflow: hidden;
    background: var(--backdrop);
    font-family: "Open Sans", sans-serif;
  }
  .canvas {
    position: relative;
    width: 1200px;
    height: 1200px;
  }
  .report-page {
    position: absolute;
    top: 255px;
    width: 430px;
    height: 609px;
    display: block;
  }
  .report-page--front { left: 122px; }
  .report-page--back { left: 647px; }
  .brand-name { font-weight: 600; fill: var(--brand-blue); letter-spacing: 0.06em; }
  .cover-title { font-weight: 600; fill: var(--paper); }
  .contact-line { font-size: 6.6px; fill: var(--ink); }
  .address-line { font-size: 6.6px; fill: var(--brand-blue); }
  .contact-icon { fill: var(--brand-blue); }
</style>
</head>
<body>
<main class="canvas">

  <!-- Front cover -->
  <svg class="report-page report-page--front" viewBox="0 0 538 761" aria-label="Report front cover">
    <rect class="page-paper" width="538" height="761" fill="var(--paper)"/>
    <polygon class="corner-wedge" points="0,0 286,0 75,325 0,325" fill="var(--steel-grey)"/>
    <rect class="accent-band" x="0" y="325" width="538" height="29" fill="var(--bright-blue)"/>
    <rect class="title-panel" x="0" y="354" width="538" height="407" fill="var(--brand-blue)"/>
    <polygon class="wedge-shadow" points="0,325 75,325 0,441" fill="var(--navy-shade)" opacity="0.85"/>

    <text class="brand-name" x="272" y="280" text-anchor="middle" font-size="30">TAVRION</text>

    <text class="cover-title" text-anchor="middle" font-size="28.5">
      <tspan x="277" y="426">LOREM IPSUM IS SIMPLY</tspan>
      <tspan x="277" y="458">DUMMY HAS BEEN</tspan>
    </text>
  </svg>

  <!-- Back cover -->
  <svg class="report-page report-page--back" viewBox="0 0 538 761" aria-label="Report back cover">
    <defs>
      <radialGradient id="patternGlow" cx="0.55" cy="0.4" r="0.6">
        <stop offset="0" stop-color="var(--pattern-tint)"/>
        <stop offset="1" stop-color="var(--brand-blue)"/>
      </radialGradient>
    </defs>
    <rect class="pattern-area" width="538" height="761" fill="url(#patternGlow)"
          role="img" aria-label="Decorative pattern of translucent triangles"/>

    <polygon class="accent-sweep" points="0,596 538,411 538,511 0,615" fill="var(--bright-blue)"/>
    <polygon class="footer-panel" points="0,615 538,511 538,761 0,761" fill="var(--paper)"/>

    <text class="brand-name" x="141" y="689" text-anchor="middle" font-size="13">TAVRION</text>

    <g class="contact-list">
      <circle class="contact-icon" cx="207" cy="666" r="4.2"/>
      <text class="contact-line" x="218" y="668.5">000-555-0142 Ext 101</text>
      <circle class="contact-icon" cx="207" cy="678" r="4.2"/>
      <text class="contact-line" x="218" y="680.5">info@tavrionmail.com</text>
      <circle class="contact-icon" cx="207" cy="690" r="4.2"/>
      <text class="contact-line" x="218" y="692.5">www.tavrionmail.com</text>
    </g>

    <line class="contact-divider" x1="311" y1="655" x2="311" y2="692" stroke="var(--brand-blue)" stroke-width="0.8"/>

    <g class="postal-address">
      <text class="address-line" x="322" y="671">210, 480 Larkspur Avenue</text>
      <text class="address-line" x="322" y="682">Northgate, Westland WL 4821</text>
    </g>
  </svg>

</main>
</body>
</html>
```